Business Card Design Project

Colette Marivaux logo on front of card with 'of Sydney' added in small font.
Back of card needs to include the following information :

"Pure pleasure for the discerning gentleman" (I may omit once I've seen the design)

colettemarivaux.com.au

Contact by SMS or email only :

colette@colettemarivaux.com.au
Mobile : 0483 956 204 or + 61 483 956 204

Target Market(s)

Male professionals aged 20-60.

Industry/Entity Type

Business

Requirements
Must have
• Simple, bold, stylish and elegant.

```html
<!DOCTYPE html>
<html lang="en">
<head>
<meta charset="utf-8">
<title>Colette Marivaux – Business Cards</title>
<link rel="stylesheet" href="https://fonts.googleapis.com/css2?family=Questrial&family=Italianno&display=swap">
<style>
  :root {
    --backdrop: #3a3a3c;
    --pattern-dark: #2a2a2c;
    --pattern-mid: #3c3c3f;
    --band-black: #0c0c0c;
    --ink: #2b2b2b;
    --ink-soft: #6a6a6a;
    --icon: #555555;
  }
  * { box-sizing: border-box; margin: 0; padding: 0; }
  html, body { width: 1200px; height: 900px; overflow: hidden; }
  body {
    background: radial-gradient(ellipse at 50% 45%, #4a4a4d 0%, var(--backdrop) 70%, #2c2c2e 100%);
    font-family: "Questrial", "Century Gothic", sans-serif;
    color: var(--ink);
    position: relative;
  }
  .card {
    position: absolute;
    width: 600px;
    height: 343px;
    border-radius: 18px;
    overflow: hidden;
    box-shadow: 0 14px 34px rgba(0,0,0,.55);
  }
  .card-art { position: absolute; inset: 0; width: 100%; height: 100%; display: block; }
  .card-front { left: 70px; top: 80px; }
  .card-back { left: 530px; top: 480px; }

  .wordmark { position: absolute; text-align: center; color: var(--ink); }
  .wordmark .name { font-size: 30px; letter-spacing: 1px; line-height: 1; }
  .wordmark .rule {
    display: block; width: 190px; height: 1px;
    background: var(--ink-soft); margin: 8px auto 6px;
  }
  .wordmark .locale { font-size: 11px; letter-spacing: .5px; color: var(--ink-soft); }
  .card-front .wordmark { left: 160px; top: 62px; width: 280px; }
  .card-back .wordmark { left: 175px; top: 72px; width: 260px; }

  .tagline {
    position: absolute;
    left: 255px;
    top: 12px;
    font-family: "Italianno", cursive;
    font-size: 26px;
    color: var(--ink);
    letter-spacing: .5px;
    white-space: nowrap;
  }
  .contact-row {
    position: absolute;
    display: flex;
    align-items: center;
    font-size: 17px;
    letter-spacing: .5px;
    white-space: nowrap;
  }
  .contact-row .icon { width: 16px; height: 16px; flex: none; margin-right: 18px; display: block; }
  .phones { left: 110px; top: 180px; }
  .phones .or { margin: 0 52px 0 56px; }
  .web { left: 110px; top: 245px; }
  .mail { left: 110px; top: 285px; }
</style>
</head>
<body>

<section class="card card-front" aria-label="Front of business card">
  <svg class="card-art" viewBox="0 0 600 343">
    <defs>
      <linearGradient id="patternTone" x1="0" y1="0" x2="1" y2="1">
        <stop offset="0" stop-color="#3c3c3f"/>
        <stop offset="1" stop-color="#2a2a2c"/>
      </linearGradient>
      <linearGradient id="flapTone" x1="0" y1="0" x2="0" y2="1">
        <stop offset="0" stop-color="#ffffff"/>
        <stop offset="1" stop-color="#e4e4e4"/>
      </linearGradient>
    </defs>
    <rect width="600" height="343" fill="url(#patternTone)" role="img" aria-label="Dark floral damask pattern"/>
    <path d="M0,0 H600 V40 C560,150 420,205 250,200 C120,196 40,175 0,150 Z" fill="#9a9a9a"/>
    <path d="M0,0 H600 V30 C555,140 420,192 250,188 C120,184 40,165 0,142 Z" fill="url(#flapTone)"/>
  </svg>
  <div class="wordmark">
    <div class="name">Colette Marivaux</div>
    <span class="rule"></span>
    <div class="locale">of Sydney</div>
  </div>
</section>

<section class="card card-back" aria-label="Back of business card">
  <svg class="card-art" viewBox="0 0 600 343">
    <defs>
      <linearGradient id="patternToneBack" x1="0" y1="0" x2="1" y2="1">
        <stop offset="0" stop-color="#3c3c3f"/>
        <stop offset="1" stop-color="#2a2a2c"/>
      </linearGradient>
      <linearGradient id="paperTone" x1="0" y1="0" x2="1" y2="1">
        <stop offset="0" stop-color="#ffffff"/>
        <stop offset="1" stop-color="#e2e2e2"/>
      </linearGradient>
    </defs>
    <rect width="600" height="343" fill="url(#paperTone)"/>
    <g role="img" aria-label="Dark floral damask pattern">
      <path d="M0,0 H215 C110,70 50,200 48,343 H0 Z" fill="url(#patternToneBack)"/>
      <path d="M600,150 C565,245 490,310 385,343 H600 Z" fill="url(#patternToneBack)"/>
    </g>
    <path d="M215,0 H245 C125,80 72,210 80,343 H48 C50,200 110,70 215,0 Z" fill="var(--band-black)"/>
    <path d="M600,110 V150 C565,245 490,310 385,343 H345 C470,300 560,230 600,110 Z" fill="var(--band-black)"/>
  </svg>

  <div class="tagline">Pure pleasure for the discerning gentleman</div>

  <div class="wordmark">
    <div class="name">Colette Marivaux</div>
    <span class="rule"></span>
    <div class="locale">of Sydney</div>
  </div>

  <div class="contact-row phones">
    <svg class="icon" viewBox="0 0 16 16" aria-label="Mobile"><rect x="4" y="1" width="8" height="14" rx="1.5" fill="none" stroke="#444" stroke-width="1.3"/><line x1="7" y1="12.5" x2="9" y2="12.5" stroke="#444" stroke-width="1.2"/></svg>
    <span>0483 956 204</span>
    <span class="or">or</span>
    <span>+ 61 483 956 204</span>
  </div>
  <div class="contact-row web">
    <svg class="icon" viewBox="0 0 16 16" aria-label="Website"><path d="M1,8 L8,2 L15,8" fill="none" stroke="#555" stroke-width="1.4"/><path d="M3.5,7.5 V14 H12.5 V7.5" fill="#777"/></svg>
    <span>colettemarivaux.com.au</span>
  </div>
  <div class="contact-row mail">
    <svg class="icon" viewBox="0 0 16 16" aria-label="Email"><text x="8" y="13" text-anchor="middle" font-family="Questrial, sans-serif" font-size="15" fill="#444">@</text></svg>
    <span>colette@colettemarivaux.com.au</span>
  </div>
</section>

</body>
</html>
```